Website Design for an Exciting, Fun & Premium Cannabis Company

Website will be designed and implemented for Wordpress with the ability to connect Plumvale Junction.
Looking to build trust with website visitors with engaging, exciting & informative content that will drive business to local dispensaries within the state of Oklahoma.
The website will embody excitement, fun, enthusiasm and make the visitor identify with the content and emphasize with a fun life they can have or believe they can have by using our products & will allow for super charged SEO and other digital marketing and advertising strategies and tactics used to increase discovery, awareness, and conversion.

Target Market(s)

Male/Female Ages 21-45

Coding

Coded - Design and coding required

Number of Pages Required

5+ page

Font styles to use
Sans Serif

Requirements
Must have
• Please see attached document for this information
Nice to have
Should not have

```html
<!DOCTYPE html>
<html lang="en">
<head>
<meta charset="utf-8">
<title>Kindle Grove — Home</title>
<link href="https://fonts.googleapis.com/css2?family=Montserrat:wght@400;500;600;700;800&display=swap" rel="stylesheet">
<style>
:root{
  --board:#87888c;
  --blue:#2430b6;
  --ink:#1d1d1f;
  --muted:#555;
  --soft:#f5f1f4;
  --white:#fff;
  --teal:#2aa58a;
  --dim:#1e1f22;
}
*{margin:0;padding:0;box-sizing:border-box}
html,body{width:1200px;height:3805px;overflow:hidden}
body{background:var(--board);font-family:'Montserrat',sans-serif;color:var(--ink);position:relative}
.abs{position:absolute}
.page{position:absolute;left:95px;top:145px;width:1000px;background:var(--white)}
section,header,footer{position:relative;overflow:hidden}
.btn{position:absolute;background:var(--blue);color:#fff;font-weight:600;display:flex;align-items:center;justify-content:center}
.sec-title{position:absolute;left:0;right:0;text-align:center;font-size:20px;font-weight:600}
.sec-title::after{content:"";display:block;width:34px;height:3px;background:var(--blue);margin:10px auto 0}
.arrow{position:absolute;width:14px;height:24px}
/* header */
.site-header{height:96px}
.brand{position:absolute;left:110px;top:30px;display:flex;align-items:center;gap:8px;font-size:20px;font-weight:700;color:var(--blue)}
.brand i{width:16px;height:16px;border-radius:50%;background:var(--blue)}
.topbar{position:absolute;top:26px;font-size:10px;font-weight:500;display:flex;align-items:center;gap:5px}
.nav{position:absolute;top:66px;left:0;font-size:11.5px;font-weight:600}
.nav a{position:absolute;color:var(--ink);text-decoration:none;white-space:nowrap}
.nav a.active{color:var(--blue);text-decoration:underline}
/* hero */
.hero{height:433px;background:linear-gradient(110deg,#3e5663 0%,#2f4652 50%,#2e4b5b 100%)}
.hero-img{position:absolute;left:0;top:0;width:620px;height:433px;background:radial-gradient(circle at 45% 48%,#2a2c2e 0 34%,#3b5360 35% 100%)}
.hero h1{position:absolute;left:656px;top:82px;font-size:32px;font-weight:800;color:#fff}
.hero p,.offer p{position:absolute;font-size:15px;line-height:21px;font-weight:500;color:#fff;width:250px}
/* categories */
.categories{height:343px}
.cat{position:absolute;top:95px;width:251px;height:200px}
.cat span{position:absolute;left:11px;bottom:10px;color:#fff;font-size:13px;font-weight:500}
.cat span::before{content:"";position:absolute;left:0;top:-8px;width:26px;height:1px;background:#fff}
.cat .btn{right:18px;bottom:0;width:62px;height:20px;font-size:8px}
/* offer */
.offer{height:399px;background:linear-gradient(90deg,#5c3a1e 0%,#8a5a2a 45%,#b07a3c 100%)}
.offer h2{position:absolute;left:682px;top:116px;font-size:23px;font-weight:700;color:#fff}
/* products */
.products{height:526px;background:var(--soft)}
.prod{position:absolute;top:108px;width:192px;height:318px;background:#fff;text-align:center}
.prod .shot{position:absolute;left:36px;top:28px;width:120px;height:170px}
.prod h3{position:absolute;left:0;right:0;top:225px;font-size:11px;font-weight:700}
.prod .price{position:absolute;left:0;right:0;top:248px;font-size:15px}
.prod .btn{left:61px;top:275px;width:70px;height:24px;font-size:8px}
.view-all{position:absolute;left:445px;top:456px;width:115px;height:27px;border:1.5px solid var(--blue);color:var(--blue);background:#fff;font-size:10px;font-weight:600;display:flex;align-items:center;justify-content:center}
/* banner */
.banner{height:427px;background:linear-gradient(90deg,#2d3a1e 0%,#56683a 40%,#8fa07a 100%)}
.banner h2{position:absolute;left:500px;top:180px;font-size:21px;line-height:31px;font-weight:800;color:#fff;width:400px}
/* reviews */
.reviews{height:315px}
.review{position:absolute;top:102px;width:247px;height:175px;background:var(--soft)}
.review p{position:absolute;left:31px;top:24px;width:190px;font-size:9.5px;line-height:14.5px;color:#333}
.review b{position:absolute;left:31px;top:140px;font-size:9.5px;font-weight:700}
.review b::before{content:"";position:absolute;left:0;top:-12px;width:26px;height:1px;background:#bbb}
/* footer */
.site-footer{height:279px;background:var(--blue);color:#fff}
.foot-brand{position:absolute;left:117px;top:95px;font-size:28px;font-weight:700;display:flex;align-items:center;gap:10px}
.foot-brand i{width:22px;height:22px;border-radius:50%;background:#fff}
.col h4{position:absolute;top:34px;font-size:10px;font-weight:700}
.menu{position:absolute;left:386px;top:64px;list-style:none;font-size:9.5px;line-height:17px}
.frow{position:absolute;display:flex;gap:10px;align-items:flex-start;font-size:9.5px;line-height:13px}
.frow i{width:19px;height:19px;border-radius:50%;background:#fff;flex:none;position:relative;top:-1px}
.frow svg{display:block;margin:4px}
.rule{position:absolute;left:110px;right:110px;top:216px;height:1px;background:rgba(255,255,255,.25)}
.copy{position:absolute;left:0;right:0;top:250px;text-align:center;font-size:8px}
/* age gate screen */
.gate{position:absolute;left:98px;top:3018px;width:1000px;height:632px;background:var(--dim);overflow:hidden}
.gate .g-head{position:absolute;left:0;top:0;width:1000px;height:96px;background:#262729}
.gate .g-hero{position:absolute;left:0;top:96px;width:1000px;height:433px;background:#1a1d20}
.ghost{position:absolute;color:#34363a;font-weight:600}
.modal{position:absolute;left:255px;top:218px;width:492px;height:227px;background:#fff;text-align:center}
.modal h2{margin-top:60px;font-size:25px;font-weight:700;letter-spacing:.3px}
.modal p{margin-top:8px;font-size:13.5px}
.modal .yes{display:inline-flex;align-items:center;justify-content:center;margin-top:24px;width:170px;height:40px;border-radius:6px;background:var(--teal);color:#fff;font-size:13px;font-weight:700}
</style>
</head>
<body>

<main class="page">
  <header class="site-header">
    <div class="brand"><i></i>Kindle Grove</div>
    <div class="topbar" style="left:549px">
      <svg width="9" height="9" viewBox="0 0 24 24"><path d="M6 2l4 4-2 3a12 12 0 007 7l3-2 4 4-3 4C10 22 2 14 2 5z" fill="#333"/></svg>888.888.8888</div>
    <div class="topbar" style="left:658px">
      <svg width="9" height="7" viewBox="0 0 24 18"><rect width="24" height="18" fill="#333"/><path d="M0 0l12 9 12-9" stroke="#fff" fill="none" stroke-width="2"/></svg>info@kindlegrove.com</div>
    <div class="abs" style="left:762px;top:22px;width:1px;height:20px;background:#ccc"></div>
    <div class="topbar" style="left:781px">My Cart
      <svg width="24" height="20" viewBox="0 0 24 20"><path d="M1 3h4l3 11h11l3-8H7" fill="none" stroke="#333" stroke-width="1.8"/><circle cx="10" cy="17.5" r="1.6" fill="#333"/><circle cx="17" cy="17.5" r="1.6" fill="#333"/></svg>
      <span class="abs" style="left:58px;top:-8px;width:12px;height:12px;border-radius:50%;background:#f15a22;color:#fff;font-size:8px;display:flex;align-items:center;justify-content:center">0</span></div>
    <svg class="abs" style="left:872px;top:24px" width="18" height="18" viewBox="0 0 24 24"><circle cx="10" cy="10" r="7" fill="none" stroke="#333" stroke-width="2.6"/><path d="M15 15l7 7" stroke="#333" stroke-width="2.8"/></svg>
    <nav class="nav">
      <a class="active" style="left:371px">Home</a><a style="left:440px">About Us</a><a style="left:531px">Services</a><a style="left:615px">Products</a><a style="left:704px">Faqs</a><a style="left:769px">Blog</a><a style="left:826px">Contact Us</a>
    </nav>
  </header>

  <section class="hero">
    <div class="hero-img" role="img" aria-label="Two CBD oil dropper bottles on a dark tray with hemp leaves"></div>
    <h1>CBD oil</h1>
    <p style="left:659px;top:132px">Lorem Ipsum is simply dummy text of the printing and type setting industry</p>
    <div class="btn" style="left:657px;top:220px;width:117px;height:43px;font-size:14px">Shop Now</div>
  </section>

  <section class="categories">
    <h2 class="sec-title" style="top:30px">Categories</h2>
    <svg class="arrow" style="left:62px;top:185px" viewBox="0 0 14 24"><path d="M11 3L3 12l8 9" fill="none" stroke="#888" stroke-width="2"/></svg>
    <div class="cat" style="left:111px;background:linear-gradient(160deg,#6b4a2e,#3a2316 60%,#6b7d4a)" role="img" aria-label="Chocolate cannabis muffins with a hemp leaf"><span>Cannabis Edibles</span><div class="btn">Shop Now</div></div>
    <div class="cat" style="left:376px;background:radial-gradient(circle at 50% 60%,#6b7a2a,#2f5a2c 70%)" role="img" aria-label="Dropper over a bottle of cannabis oil among leaves"><span>Cannabis Oil</span><div class="btn">Shop Now</div></div>
    <div class="cat" style="left:640px;background:linear-gradient(140deg,#a3202a,#3a2418 55%,#c8a04a)" role="img" aria-label="Red and yellow gummies with cannabis buds"><span>Gummies</span><div class="btn">Shop Now</div></div>
    <svg class="arrow" style="left:918px;top:185px" viewBox="0 0 14 24"><path d="M3 3l8 9-8 9" fill="none" stroke="#888" stroke-width="2"/></svg>
  </section>

  <section class="offer">
    <div class="abs" style="left:0;top:0;width:560px;height:399px;background:linear-gradient(120deg,#e9c9b0 0%,#9a1e2e 40%,#7a1526 70%,#8a5a2a 100%)" role="img" aria-label="Hand holding a gummy ring in front of a CBD infused gummy bag"></div>
    <h2>50% Special Offers</h2>
    <p style="left:682px;top:158px;width:250px">Lorem Ipsum is simply dummy text of the printing and type setting industry</p>
    <div class="btn" style="left:682px;top:244px;width:115px;height:43px;font-size:14px">Shop Now</div>
  </section>

  <section class="products">
    <h2 class="sec-title" style="top:36px">Our Products</h2>
    <svg class="arrow" style="left:59px;top:257px" viewBox="0 0 14 24"><path d="M11 3L3 12l8 9" fill="none" stroke="#888" stroke-width="2"/></svg>
    <div class="prod" style="left:98px"><div class="shot" role="img" aria-label="Pack of colourful leaf-shaped gummies" style="background:linear-gradient(135deg,#d9473a,#e8a030,#3f8a3a)"></div><h3>LOREM IPSUM</h3><div class="price">$20.00</div><div class="btn">Shop Now</div></div>
    <div class="prod" style="left:303px"><div class="shot" role="img" aria-label="Green CBD pouch" style="background:linear-gradient(160deg,#6fd24a,#3fae2e)"></div><h3>LOREM IPSUM</h3><div class="price">$20.00</div><div class="btn">Shop Now</div></div>
    <div class="prod" style="left:505px"><div class="shot" role="img" aria-label="Amber oil bottle beside cannabis buds and a vape pen" style="background:linear-gradient(180deg,#fff 20%,#8a4a1a 55%,#5a6a3a)"></div><h3>LOREM IPSUM</h3><div class="price">$20.00</div><div class="btn">Shop Now</div></div>
    <div class="prod" style="left:709px"><div class="shot" role="img" aria-label="Silver pouch with cannabis flower" style="background:linear-gradient(160deg,#e4e4e4,#9a9a9a 60%,#6a7a4a)"></div><h3>LOREM IPSUM</h3><div class="price">$20.00</div><div class="btn">Shop Now</div></div>
    <svg class="arrow" style="left:926px;top:257px" viewBox="0 0 14 24"><path d="M3 3l8 9-8 9" fill="none" stroke="#888" stroke-width="2"/></svg>
    <div class="view-all">View all products</div>
  </section>

  <section class="banner">
    <div class="abs" style="inset:0" role="img" aria-label="Vape cartridge with amber oil among cannabis buds"></div>
    <h2>LOREM IPSUM IS SIMPLY DUMMY TEXT OF THE PRINTING AND TYPESETTING INDUSTRY</h2>
    <div class="btn" style="left:500px;top:293px;width:115px;height:40px;font-size:14px">Shop Now</div>
  </section>

  <section class="reviews">
    <h2 class="sec-title" style="top:35px">Reviews</h2>
    <svg class="arrow" style="left:66px;top:178px" viewBox="0 0 14 24"><path d="M11 3L3 12l8 9" fill="none" stroke="#888" stroke-width="2"/></svg>
    <div class="review" style="left:111px"><p>There are many variations of passages of Lorem Ipsum available, but the majority have suffered alteration in some form, by injected humour, or randomised words which don't look even slightly believable</p><b>RICHARD</b></div>
    <div class="review" style="left:378px"><p>There are many variations of passages of Lorem Ipsum available, but the majority have suffered alteration in some form, by injected humour, or randomised words which don't look even slightly believable</p><b>RICHARD</b></div>
    <div class="review" style="left:643px"><p>There are many variations of passages of Lorem Ipsum available, but the majority have suffered alteration in some form, by injected humour, or randomised words which don't look even slightly believable</p><b>RICHARD</b></div>
    <svg class="arrow" style="left:918px;top:178px" viewBox="0 0 14 24"><path d="M3 3l8 9-8 9" fill="none" stroke="#888" stroke-width="2"/></svg>
  </section>

  <footer class="site-footer">
    <div class="foot-brand"><i></i>Kindle Grove</div>
    <div class="col"><h4 style="left:386px">MENU</h4></div>
    <ul class="menu"><li>HOME</li><li>ABOUT US</li><li>SERVICES</li><li>PRODUCTS</li><li>FAQS</li><li>BLOG</li><li>CONTACT US</li></ul>
    <div class="col"><h4 style="left:568px">CONTACT US</h4></div>
    <div class="frow" style="left:568px;top:70px"><i><svg width="11" height="11" viewBox="0 0 24 24"><path d="M12 2a7 7 0 00-7 7c0 5 7 13 7 13s7-8 7-13a7 7 0 00-7-7z" fill="#2430b6"/></svg></i><span>2150 Larkspur Avenue<br>Fairmont, CA 90000</span></div>
    <div class="frow" style="left:568px;top:113px"><i><svg width="11" height="11" viewBox="0 0 24 24"><path d="M6 2l4 4-2 3a12 12 0 007 7l3-2 4 4-3 4C10 22 2 14 2 5z" fill="#2430b6"/></svg></i><span>Call Us<br>888.888.8888</span></div>
    <div class="frow" style="left:568px;top:156px"><i><svg width="11" height="11" viewBox="0 0 24 24"><rect x="2" y="5" width="20" height="14" fill="#2430b6"/><path d="M2 5l10 8 10-8" stroke="#fff" fill="none" stroke-width="2"/></svg></i><span>E mail Us<br>info@kindlegrove.com</span></div>
    <div class="col"><h4 style="left:803px">FOLLOW US</h4></div>
    <div class="frow" style="left:803px;top:70px"><i></i><span>Like us on<br>FRIENDLOOP</span></div>
    <div class="frow" style="left:803px;top:112px"><i></i><span>Follow us on<br>CHIRPER</span></div>
    <div class="frow" style="left:803px;top:154px"><i></i><span>Follow us on<br>WORKNET</span></div>
    <div class="rule"></div>
    <div class="copy">Copyright © 2021 All Rights Reserved</div>
  </footer>
</main>

<div class="gate">
  <div class="g-head"></div>
  <div class="ghost" style="left:110px;top:30px;font-size:20px">Kindle Grove</div>
  <div class="ghost" style="left:371px;top:66px;font-size:11.5px;word-spacing:40px">Home About Services Products Faqs Blog Contact</div>
  <div class="g-hero"></div>
  <div class="ghost" style="left:656px;top:178px;font-size:32px;font-weight:800">CBD oil</div>
  <div class="ghost" style="left:0;right:0;top:572px;text-align:center;font-size:20px">Categories</div>
  <div class="modal">
    <h2>AGE VERIFICATION</h2>
    <p>Please verify your age before shopping our products!</p>
    <div class="yes">YES, I AM OVER 21</div>
  </div>
</div>

</body>
</html>
```